Modern Label for cleaning products for the brand Voralux

We need a label design for our line of cleaning products. The label should feature our logo and an image to identify the product's intended use. I've added our logo and an image for use. This only concerns the design of the label on the front of the bottle.

Label dimensions:
Label 1 (500ml bottle with spray): width 58mm x height 115mm
Label 2: (1L bottle): width 73mm x height 140mm
The design must be consistent for both bottles which you find in the pictures.

The bottles to be labeled are white. See the attachment for a photo of the bottles.

The photo must also appear on the label to identify the product's intended use.

Product information:
Brand: Voralux
Product: Sanitary Cleaner

This text must be placed on the label:
"Cleans, descales & freshens. followed with this text: "Ideal for quick and powerful cleaning. A ready-to-use product for everyday use."

- Mention the seperate USP's: Sanitary, Bathroom, Toilet, Wet areas

Appearance: This is a consumer product, but it must have a professional appearance. We would like to see a design that use the color blue from our logo.

Target Market(s)

Consumers who take care of their homes and want to maintain it the correct (professional) way

Font styles to use
Sans Serif

Colors
0054AA
0677BA
7BADD7
CADEEF
E8F1F8

Requirements
Must have
• USP's + use of image and logo + blend in 1 design
Nice to have
• Keep the color of the logo in the design
Should not have
• Comic sans

```html
<!DOCTYPE html>
<html lang="en">
<head>
<meta charset="utf-8">
<title>Voralux Sanitary Cleaner – Front Label</title>
<link rel="stylesheet" href="https://fonts.googleapis.com/css2?family=Poppins:wght@400;600;700;800&display=swap">
<style>
  :root {
    --blue-deep: #0054AA;
    --blue-mid: #0677BA;
    --blue-bright: #0B8FD6;
    --blue-soft: #7BADD7;
    --blue-pale: #CADEEF;
    --blue-mist: #E8F1F8;
    --ink: #111418;
    --paper: #FFFFFF;
    --stage: #ECEEF0;
  }
  * { margin: 0; padding: 0; box-sizing: border-box; }
  html, body {
    width: 1200px;
    height: 545px;
    overflow: hidden;
    background: var(--stage);
    font-family: "Poppins", sans-serif;
  }
  .canvas {
    position: relative;
    width: 1200px;
    height: 545px;
    display: flex;
    align-items: center;
    justify-content: center;
  }
  .label {
    position: relative;
    width: 250px;
    height: 500px;
    border-radius: 22px;
    background: var(--paper);
    overflow: hidden;
  }
  .label__artwork {
    position: absolute;
    inset: 0;
  }
  .brand {
    position: absolute;
    top: 18px;
    left: 0;
    right: 0;
    display: flex;
    flex-direction: column;
    align-items: center;
    gap: 6px;
  }
  .brand__dot {
    width: 36px;
    height: 36px;
    border-radius: 50%;
    border: 4px solid var(--blue-mid);
  }
  .brand__name {
    font-weight: 600;
    font-size: 18px;
    line-height: 1;
    color: var(--ink);
    letter-spacing: 0.2px;
  }
  .claim {
    position: absolute;
    top: 354px;
    left: 0;
    right: 0;
    text-align: center;
    font-weight: 700;
    font-size: 11.5px;
    line-height: 1.25;
    color: var(--ink);
  }
  .description {
    position: absolute;
    top: 393px;
    left: 0;
    right: 0;
    text-align: center;
    font-weight: 400;
    font-size: 6.6px;
    line-height: 1.25;
    color: var(--paper);
  }
  .usp-list {
    position: absolute;
    left: 29px;
    top: 445px;
    list-style: none;
    font-weight: 700;
    font-size: 8px;
    line-height: 1.22;
    color: var(--paper);
  }
  .usp-list li::before {
    content: "\2022\00a0";
  }
  .volume-tab {
    position: absolute;
    left: 175px;
    bottom: 0;
    width: 44px;
    height: 56px;
    background: var(--paper);
    border-radius: 22px 22px 0 0;
    display: flex;
    align-items: center;
    justify-content: center;
    padding-top: 10px;
    font-weight: 700;
    font-size: 9px;
    color: var(--ink);
  }
</style>
</head>
<body>
<main class="canvas">
  <article class="label">
    <svg class="label__artwork" width="250" height="500" viewBox="0 0 250 500">
      <defs>
        <linearGradient id="panelBlue" x1="0" y1="0" x2="0" y2="1">
          <stop offset="0" stop-color="var(--blue-bright)"/>
          <stop offset="0.55" stop-color="#0A86CF"/>
          <stop offset="1" stop-color="var(--blue-mid)"/>
        </linearGradient>
        <linearGradient id="photoTone" x1="0" y1="0" x2="0" y2="1">
          <stop offset="0" stop-color="#E6E8EA"/>
          <stop offset="0.55" stop-color="#C9CCCF"/>
          <stop offset="1" stop-color="#A9ACAF"/>
        </linearGradient>
        <path id="titleArc" d="M 31 193 A 100 100 0 1 1 222 253"/>
      </defs>

      <path class="panel" d="M 0 227 A 125 125 0 0 1 250 227 L 250 500 L 0 500 Z" fill="url(#panelBlue)"/>

      <text font-family="Poppins, sans-serif" font-weight="800" font-size="23" letter-spacing="1.2">
        <textPath href="#titleArc" startOffset="1%"><tspan fill="#FFFFFF">SANITARY </tspan><tspan fill="#111418">CLEANER</tspan></textPath>
      </text>

      <circle cx="125" cy="227" r="89" fill="#FFFFFF"/>
      <circle cx="125" cy="227" r="86" fill="url(#photoTone)" role="img" aria-label="Photo of a clean modern bathroom with walk-in shower, vanity and grey tiled floor"/>
    </svg>

    <header class="brand">
      <span class="brand__dot"></span>
      <span class="brand__name">Voralux</span>
    </header>

    <p class="claim">Cleans, descales &amp;<br>freshens.</p>
    <p class="description">Ideal for quick and powerful<br>cleaning. A ready-to-use product<br>for everyday use.</p>

    <ul class="usp-list">
      <li>Sanitary</li>
      <li>Bathroom</li>
      <li>Toilet</li>
      <li>Wet areas</li>
    </ul>

    <div class="volume-tab">500ml</div>
  </article>
</main>
</body>
</html>
```